Environmentally friendly Home and Office cleaning service needs a logo and web design!

Tidewell Housekeeping is a new startup looking for a logo and web design. We're base in Ottawa, Canada, and all of our products are eco-friendly, as well as being easy on the sensitivities of our clients.
We wash windows, walls, kitchens, bathrooms, dust, vacuum and wash floors on our hands and knees, and bring all of our own gear and supplies.
plumrake.example was my last website. It's functional, not bad - but just isn't great. I'm looking for a simple design, with few links or clickable buttons.
Colours I will leave to your creative mind to decide. I just want to see something that is relevant to "Tidewell Housekeeping."

Target Market(s)

Often it's women and gay men, ages 35-70
White collar government workers, usually with pets (cats, dogs)

Industry/Entity Type

Cleaning Service

Logo Text

Tidewell Housekeeping

Number of Pages Required

1 page

Font styles to use
Sans Serif

Colors

Designer to choose colors to be used in the design.

Requirements
Must have
• Colour, pictures

```html
<!DOCTYPE html>
<html lang="en">
<head>
<meta charset="utf-8">
<title>Tidewell Housekeeping</title>
<link rel="stylesheet" href="https://fonts.googleapis.com/css2?family=Raleway:wght@400;500;600;700&family=Roboto:wght@400;500;700&display=swap">
<style>
  :root {
    --blue: #2f6db3;
    --navy: #0d4a8a;
    --orange: #f07426;
    --green: #57b04a;
    --green-light: #6cb85a;
    --ink: #2b2b2b;
    --body: #4a4a4a;
    --white: #ffffff;
  }
  * { box-sizing: border-box; margin: 0; padding: 0; }
  html, body { width: 1200px; height: 2740px; overflow: hidden; }
  body { position: relative; background: var(--white); font-family: "Raleway", sans-serif; color: var(--body); }
  .abs { position: absolute; }

  /* Hero */
  .hero { left: 0; top: 0; width: 1200px; height: 663px;
    background: linear-gradient(160deg, #d9d4c8 0%, #b9b2a4 35%, #8d8476 70%, #a39a8a 100%); }
  .topbar { left: 0; top: 0; width: 1200px; height: 113px; background: rgba(104, 170, 96, 0.72); }
  .brand { left: 88px; top: 46px; display: flex; align-items: center; gap: 12px;
    font-family: "Raleway", sans-serif; font-weight: 600; font-size: 26px; color: var(--white); }
  .brand-dot { width: 22px; height: 22px; border-radius: 50%; background: var(--white); }
  .top-phone { left: 606px; top: 65px; display: flex; align-items: center; gap: 12px;
    font-family: "Roboto", sans-serif; font-size: 15px; color: var(--white); }
  .search { left: 785px; top: 60px; width: 225px; height: 24px; border-bottom: 1px solid var(--white);
    font-family: "Roboto", sans-serif; font-size: 12px; color: var(--white); }
  .search svg { position: absolute; right: 2px; top: 2px; }
  .menu { left: 1040px; top: 66px; display: flex; align-items: center; gap: 10px;
    font-family: "Roboto", sans-serif; font-size: 15px; color: var(--white); }
  .socials-top { left: 990px; top: 8px; display: flex; gap: 14px; }
  .socials-top span { width: 14px; height: 14px; border-radius: 50%; background: var(--white); }
  .hero-title { left: 0; top: 328px; width: 1200px; text-align: center;
    font-family: "Roboto", sans-serif; font-weight: 700; font-size: 42px; color: var(--white);
    text-shadow: 0 2px 6px rgba(0,0,0,0.45); letter-spacing: 0.5px; }

  /* Services strip */
  .services { left: 0; top: 663px; width: 1200px; height: 200px; }
  .service-label { position: absolute; top: 74px; width: 200px; text-align: center;
    font-family: "Roboto", sans-serif; font-size: 25px; color: var(--white); }
  .service-icon { position: absolute; top: 24px; }
  .we-wash { position: absolute; left: 20px; top: 72px; display: flex; align-items: center; gap: 8px;
    font-family: "Roboto", sans-serif; font-weight: 700; font-size: 25px; color: var(--white); }

  /* Intro */
  .intro { left: 0; top: 928px; width: 1200px; text-align: center; }
  .intro h2 { font-family: "Roboto", sans-serif; font-weight: 700; font-size: 30px; color: var(--ink); letter-spacing: 0.3px; }
  .intro .accent { font-family: "Roboto", sans-serif; font-weight: 400; font-size: 30px; color: var(--orange); margin-top: 4px; }
  .divider { margin: 16px auto 0; width: 290px; height: 24px; }
  .intro-copy { width: 1010px; margin: 26px auto 0; font-size: 15.5px; line-height: 26px; color: var(--body); }
  .intro-copy p + p { margin-top: 26px; }

  /* Eco section */
  .eco { left: 0; top: 1351px; width: 1200px; height: 362px;
    background: linear-gradient(120deg, #c7692a 0%, #8a4a22 45%, #3b2f2a 70%, #d8d4cf 100%); }
  .eco-panel { left: 0; top: 1351px; }
  .eco h3 { position: absolute; left: 91px; top: 36px; font-family: "Raleway", sans-serif; font-weight: 600; font-size: 29px; color: var(--white); }
  .eco ul { position: absolute; left: 91px; top: 110px; list-style: none; }
  .eco li { display: flex; gap: 14px; font-size: 17.5px; line-height: 27px; color: var(--white); margin-bottom: 18px; }
  .eco li svg { flex: none; margin-top: 5px; }

  /* How it works */
  .how-photo { left: 0; top: 1713px; width: 599px; height: 593px;
    background: linear-gradient(135deg, #e9e6e1 0%, #c9bda9 40%, #8f7a5f 75%, #d7d0c4 100%); }
  .how-card { left: 447px; top: 1782px; width: 753px; height: 482px; background: var(--green); color: var(--white); }
  .how-card h3 { position: absolute; left: 35px; top: 28px; font-family: "Raleway", sans-serif; font-weight: 700; font-size: 31px; }
  .how-card h4 { position: absolute; left: 37px; top: 70px; font-family: "Raleway", sans-serif; font-weight: 700; font-size: 21px; }
  .how-card .rule { position: absolute; left: 37px; top: 104px; width: 74px; height: 3px; background: var(--orange); }
  .how-list { position: absolute; left: 37px; top: 132px; width: 670px; font-size: 14.5px; line-height: 23px; }
  .how-list .item { position: relative; padding-left: 46px; margin-bottom: 18px; }
  .how-list .item svg { position: absolute; left: 0; top: 0; }

  /* About */
  .about { left: 86px; top: 2372px; width: 1024px; }
  .about h3 { font-family: "Raleway", sans-serif; font-weight: 700; font-size: 25px; color: var(--navy); }
  .about p { font-size: 13.5px; line-height: 26px; color: var(--ink); }
  .about .hi { margin-top: 12px; }

  /* Footer */
  .footer { left: 0; top: 2580px; width: 1200px; height: 113px; background: var(--navy); }
  .pill { position: absolute; top: 33px; height: 47px; border: 1.5px solid rgba(255,255,255,0.75); border-radius: 24px;
    display: flex; align-items: center; justify-content: center; gap: 14px;
    font-family: "Roboto", sans-serif; font-size: 18px; color: var(--white); }
  .pill .dot { width: 18px; height: 18px; border-radius: 50%; background: var(--white); }
  .copyright { left: 0; top: 2693px; width: 1200px; height: 47px; background: var(--green-light);
    display: flex; align-items: center; justify-content: center; font-size: 12.5px; color: rgba(255,255,255,0.85); }
</style>
</head>
<body>

  <!-- Hero -->
  <div class="abs hero" role="img" aria-label="Photo of a cleaner in a green apron mopping a bright living room floor"></div>
  <div class="abs topbar"></div>
  <div class="abs brand"><span class="brand-dot"></span>Tidewell Housekeeping</div>
  <div class="abs top-phone">
    <svg width="24" height="20" viewBox="0 0 24 20"><path d="M3 7c0-3 4-5 9-5s9 2 9 5l-4 1-1-3H8L7 8Z" fill="#fff"/><rect x="5" y="10" width="14" height="8" rx="2" fill="#fff"/><circle cx="12" cy="14" r="2.2" fill="#7ab06f"/></svg>
    613-555-0142
  </div>
  <div class="abs search">Search
    <svg width="14" height="14" viewBox="0 0 14 14"><circle cx="6" cy="6" r="4.3" fill="none" stroke="#fff" stroke-width="1.8"/><line x1="9" y1="9" x2="13" y2="13" stroke="#fff" stroke-width="1.8"/></svg>
  </div>
  <div class="abs menu">Menu
    <svg width="24" height="18" viewBox="0 0 24 18"><rect y="0" width="24" height="3" fill="#fff"/><rect y="7.5" width="24" height="3" fill="#fff"/><rect y="15" width="24" height="3" fill="#fff"/></svg>
  </div>
  <div class="abs socials-top"><span></span><span></span><span></span><span></span></div>
  <h1 class="abs hero-title">WELCOME TO TIDEWELL HOUSEKEEPING</h1>

  <!-- Services -->
  <div class="abs services">
    <svg width="1200" height="200" viewBox="0 0 1200 200" style="position:absolute;left:0;top:0">
      <polygon points="0,0 200,0 200,155 0,200" fill="var(--blue)"/>
      <polygon points="200,0 400,0 400,200 200,155" fill="var(--orange)"/>
      <polygon points="400,0 600,0 600,155 400,200" fill="var(--blue)"/>
      <polygon points="600,0 800,0 800,200 600,155" fill="var(--orange)"/>
      <polygon points="800,0 1000,0 1000,155 800,200" fill="var(--blue)"/>
      <polygon points="1000,0 1200,0 1200,200 1000,155" fill="var(--orange)"/>
    </svg>
    <div class="we-wash">WE WASH
      <svg width="28" height="24" viewBox="0 0 28 24"><path d="M2 9h13V2l11 10-11 10v-7H2Z" fill="#fff"/></svg>
    </div>
    <svg class="service-icon" style="left:270px" width="60" height="48" viewBox="0 0 60 48" fill="none" stroke="#fff" stroke-width="2.5"><rect x="4" y="14" width="52" height="30"/><line x1="30" y1="14" x2="30" y2="44"/><path d="M20 14V6h20v8"/><line x1="12" y1="24" x2="22" y2="24"/><line x1="38" y1="24" x2="48" y2="24"/></svg>
    <div class="service-label" style="left:200px">Kitchens</div>
    <svg class="service-icon" style="left:468px" width="64" height="50" viewBox="0 0 64 50" fill="none" stroke="#fff" stroke-width="2.5"><path d="M6 24h52v8c0 7-6 12-13 12H19C12 44 6 39 6 32Z"/><path d="M12 24V8a5 5 0 0 1 10 0"/><line x1="16" y1="44" x2="13" y2="49"/><line x1="48" y1="44" x2="51" y2="49"/></svg>
    <div class="service-label" style="left:400px">Bathrooms</div>
    <svg class="service-icon" style="left:666px" width="68" height="50" viewBox="0 0 68 50" fill="none" stroke="#fff" stroke-width="2.5"><path d="M8 44c0-14 10-24 26-24s26 10 26 24Z"/><line x1="34" y1="20" x2="20" y2="4"/><circle cx="48" cy="36" r="5"/></svg>
    <div class="service-label" style="left:600px">Floors</div>
    <svg class="service-icon" style="left:878px" width="44" height="56" viewBox="0 0 44 56" fill="none" stroke="#fff" stroke-width="2.5"><path d="M4 54V20a18 18 0 0 1 36 0v34Z"/><line x1="22" y1="2" x2="22" y2="54"/><line x1="4" y1="28" x2="40" y2="28"/><line x1="4" y1="41" x2="40" y2="41"/></svg>
    <div class="service-label" style="left:800px">Windows</div>
    <svg class="service-icon" style="left:1062px" width="76" height="52" viewBox="0 0 76 52"><path d="M4 34 40 22 72 34 36 48Z" fill="#fff"/><path d="M4 22 40 10 72 22 36 36Z" fill="#fff" stroke="var(--orange)" stroke-width="2"/><path d="M8 12 40 2 68 12 36 24Z" fill="#fff" stroke="var(--orange)" stroke-width="2"/></svg>
    <div class="service-label" style="left:1000px">Walls</div>
  </div>

  <!-- Intro -->
  <section class="abs intro">
    <h2>LET US BE PART OF YOUR TEAM TO KEEP</h2>
    <div class="accent">YOUR SPACE CLEAN!</div>
    <svg class="divider" viewBox="0 0 290 24"><line x1="0" y1="12" x2="125" y2="12" stroke="var(--blue)" stroke-width="1.5"/><line x1="165" y1="12" x2="290" y2="12" stroke="var(--blue)" stroke-width="1.5"/><line x1="140" y1="18" x2="154" y2="3" stroke="var(--orange)" stroke-width="2.5"/><path d="M134 16l8 6 4-6-6-4Z" fill="var(--orange)"/></svg>
    <div class="intro-copy">
      <p>We will give your home the respect it deserves with careful attention to detail and thorough work. It can be a relief to know that you can leave and come back and never have to worry about dusting, vacuuming, windows or walls.</p>
      <p>We do all of that for you!<br>You don't even have to think about providing any materials for us since we supply all of our own gear and equipment, all of which is 100% eco-friendly and kind on sensitivities.</p>
      <p>We are insured and have references available to confirm our work ethic and trustworthiness.</p>
    </div>
  </section>

  <!-- Eco -->
  <section class="abs eco" role="img" aria-label="Photo of a gloved hand wiping a kitchen counter with a cloth">
    <svg width="1200" height="362" viewBox="0 0 1200 362" style="position:absolute;left:0;top:0">
      <polygon points="0,0 858,0 730,362 0,362" fill="var(--orange)" opacity="0.88"/>
      <line x1="846" y1="0" x2="718" y2="362" stroke="#2b2420" stroke-width="4"/>
      <line x1="866" y1="0" x2="738" y2="362" stroke="#2b2420" stroke-width="4"/>
    </svg>
    <h3>What Makes Tidewell Housekeeping Environmentally Friendly?</h3>
    <ul>
      <li><svg width="18" height="18" viewBox="0 0 18 18" fill="none" stroke="#fff" stroke-width="1.5"><circle cx="9" cy="9" r="5"/><line x1="9" y1="0" x2="9" y2="18"/><line x1="0" y1="9" x2="18" y2="9"/></svg>We use unscented, non-toxic, chemical-free cleaners</li>
      <li><svg width="18" height="18" viewBox="0 0 18 18" fill="none" stroke="#fff" stroke-width="1.5"><circle cx="9" cy="9" r="5"/><line x1="9" y1="0" x2="9" y2="18"/><line x1="0" y1="9" x2="18" y2="9"/></svg>We use vinegar as an antiseptic and deodorizer when needed,<br>as well as for windows and mirrors</li>
      <li><svg width="18" height="18" viewBox="0 0 18 18" fill="none" stroke="#fff" stroke-width="1.5"><circle cx="9" cy="9" r="5"/><line x1="9" y1="0" x2="9" y2="18"/><line x1="0" y1="9" x2="18" y2="9"/></svg>We use baking soda if we need more aggressive scrubbing</li>
      <li><svg width="18" height="18" viewBox="0 0 18 18" fill="none" stroke="#fff" stroke-width="1.5"><circle cx="9" cy="9" r="5"/><line x1="9" y1="0" x2="9" y2="18"/><line x1="0" y1="9" x2="18" y2="9"/></svg>We use a HEPA-filter vacuum for allergen relief</li>
    </ul>
  </section>

  <!-- How it works -->
  <div class="abs how-photo" role="img" aria-label="Photo of two cleaners in yellow gloves tidying a living room"></div>
  <section class="abs how-card">
    <h3>How it Works</h3>
    <h4>The first clean is half-off because:</h4>
    <div class="rule"></div>
    <div class="how-list">
      <div class="item"><svg width="32" height="22" viewBox="0 0 32 22" fill="none" stroke="#fff" stroke-width="1.6"><path d="M2 9h18l8-4M2 9v10h16l3-4"/><path d="M20 9l9 0"/></svg>We don't give estimates. Houses can be very deceiving, and we don't want to set inappropriate expectations. The discounted rate gives us the ability to estimate just how long regular cleans will take.</div>
      <div class="item"><svg width="32" height="22" viewBox="0 0 32 22" fill="none" stroke="#fff" stroke-width="1.6"><path d="M2 9h18l8-4M2 9v10h16l3-4"/><path d="M20 9l9 0"/></svg>This also gives you the chance to test us out and see if we're a good fit.</div>
      <div class="item">For the first clean, it'd be ideal if you were there so that we can go room to room and make sure everything is exactly as you like it to be. I don't want us leaving until you're happy!</div>
      <div class="item">Assuming you like what you see, we can then schedule regular appointments. I will have a copy of your keys made and initial them so that no one knows who these keys belong to (Jane Doe would be "JD").</div>
    </div>
  </section>

  <!-- About -->
  <section class="abs about">
    <h3>Who Am I?</h3>
    <p class="hi">Hi!</p>
    <p>My name is Marcel Avery and I have been a professional cleaner in the Ottawa area for over 2 years, under the tutelage of Ellis Warren, another professional with more than 15 years experience in the field. He taught me everything he knows about what clients want from their cleaners: a meticulous eye for detail, reliability and to always search for the difference that makes a difference in the client's eyes.</p>
  </section>

  <!-- Footer -->
  <footer class="abs footer">
    <div class="pill" style="left:86px;width:215px">
      <svg width="26" height="22" viewBox="0 0 24 20"><path d="M3 7c0-3 4-5 9-5s9 2 9 5l-4 1-1-3H8L7 8Z" fill="#fff"/><rect x="5" y="10" width="14" height="8" rx="2" fill="#fff"/><circle cx="12" cy="14" r="2.2" fill="var(--navy)"/></svg>
      613-555-0142
    </div>
    <div class="pill" style="left:420px;width:360px">
      <svg width="24" height="20" viewBox="0 0 24 20" fill="none" stroke="#fff" stroke-width="1.6"><rect x="2" y="3" width="20" height="15"/><path d="M2 3l10 8 10-8"/></svg>
      marcel.avery@plumrake.example
    </div>
    <div class="pill" style="left:897px;width:215px;gap:26px">
      <span class="dot"></span><span class="dot"></span><span class="dot"></span><span class="dot"></span>
    </div>
  </footer>
  <div class="abs copyright">© Copyright 2017 Tidewell Housekeeping | All Rights Reserved.</div>

</body>
</html>
```